The ONLY 100% Free Security System

We are a national home/auto insurance agency that will be offering home security systems. Our "pitch" is that we will show people (before signing any agreements) how much they can save on their home/auto insurance based on having a security system installed. This is often enough to completely offset the cost of the monthly monitoring fee. One side of the flyer will highlight "The ONLY 100% truly free security system". The other side will list the following bullet points: 1. $100's in FREE Premium Security Equipment 2. FREE Professional Installation 3. "and what no other company offers..." ZERO Cost Monitoring (up to a $74.95 per month value) How? Call our 24-hour message line for a 2-minute overview: (phone # needs to be editable)

The last bullet point (what no other company offers... ZERO cost monitoring) needs to stand out.

Target Market(s)

Homeowners and businesses

Industry/Entity Type

Insurance

Font styles to use
Serif
Sans Serif

Colors

Designer to choose colors to be used in the design.

Requirements
Must have
• Editable phone # - this is also a 5.5"(width) X 8.5" (length) flyer

```html
<!DOCTYPE html>
<html lang="en">
<head>
<meta charset="utf-8">
<title>Shieldwise – The Only 100% Free Security System</title>
<link rel="stylesheet" href="https://fonts.googleapis.com/css2?family=Lato:wght@400;700&family=Oswald:wght@600;700&family=Roboto:wght@700&display=swap">
<style>
  :root {
    --brand-blue: #1a47a8;
    --deep-blue: #1d3f9a;
    --brand-green: #17943a;
    --ink: #1b1b1b;
    --footer: #2c2c2c;
    --page: #e9eaec;
    --sky-top: #8fd0f0;
    --sky-mid: #cdeaf8;
    --card: #ffffff;
  }
  * { margin: 0; padding: 0; box-sizing: border-box; }
  html, body { width: 1200px; height: 903px; overflow: hidden; background: var(--page); }
  body { position: relative; font-family: "Lato", sans-serif; color: var(--ink); }

  .flyer {
    position: absolute; top: 96px; width: 434px; height: 662px;
    background: var(--card); overflow: hidden;
    box-shadow: 0 6px 18px rgba(0,0,0,.18);
  }
  .flyer--front { left: 117px; }
  .flyer--back { left: 639px; width: 436px; }

  /* Front */
  .hero-photo {
    position: absolute; left: 0; top: 0; width: 100%; height: 318px;
    background: linear-gradient(180deg, var(--sky-top) 0%, var(--sky-mid) 55%, #f4fbff 100%);
  }
  .hero-curve { position: absolute; left: 0; top: 290px; width: 434px; height: 40px; }

  .brand { position: absolute; left: 0; width: 100%; text-align: center; }
  .brand--front { top: 370px; }
  .brand__name {
    font-family: "Lato", sans-serif; font-weight: 700; color: var(--brand-blue);
    font-size: 36px; line-height: 1; display: inline-flex; align-items: center; gap: 8px;
  }
  .brand__dot { width: 12px; height: 12px; border-radius: 50%; background: var(--brand-green); display: inline-block; }

  .headline-box {
    position: absolute; left: 57px; top: 463px; width: 319px; height: 139px;
    border: 1px solid #a8a8a8; border-radius: 6px;
  }
  .headline { position: absolute; left: 0; top: 0; width: 100%; height: 100%; font-family: "Oswald", sans-serif; font-weight: 700; }
  .headline__line { position: absolute; left: 0; width: 100%; text-align: center; line-height: 1; white-space: nowrap; }
  .headline__only { top: 437px; }
  .headline__only span { background: var(--card); padding: 0 12px; color: var(--brand-green); font-size: 48px; }
  .headline__free { top: 482px; color: var(--deep-blue); font-size: 60px; letter-spacing: 0.5px; }
  .headline__system { top: 550px; color: var(--brand-green); font-size: 40px; }

  .footer-bar {
    position: absolute; left: 0; bottom: 0; width: 100%; height: 34px; background: var(--footer);
    color: #fff; font-size: 12px; letter-spacing: 2.6px; text-align: center; line-height: 34px;
  }

  /* Back */
  .sky-panel {
    position: absolute; left: 0; top: 0; width: 100%; height: 454px;
    background: linear-gradient(180deg, #e6f4fc 0%, #cfe9f8 45%, #bfe2f6 100%);
  }
  .benefit { position: absolute; left: 0; width: 100%; height: 100px; }
  .benefit__icon { position: absolute; left: 41px; width: 98px; height: 98px; }
  .benefit__text { position: absolute; left: 172px; }
  .benefit__title { font-size: 33px; font-weight: 700; color: var(--brand-blue); line-height: 1; white-space: nowrap; }
  .benefit__title--sm { font-size: 23px; }
  .benefit__note { font-size: 16px; font-weight: 700; color: var(--ink); margin-top: 4px; white-space: nowrap; }
  .benefit__note--light { font-weight: 400; }
  .accent-green { color: var(--brand-green); }
  .benefit--equipment { top: 31px; }
  .benefit--equipment .benefit__text { top: 22px; }
  .benefit--install { top: 181px; }
  .benefit--install .benefit__text { top: 23px; }
  .benefit--monitoring { top: 330px; }
  .benefit--monitoring .benefit__text { top: 27px; }

  .how-question {
    position: absolute; left: 0; top: 466px; width: 100%; text-align: center;
    font-family: "Roboto", sans-serif; font-weight: 700; font-size: 14px; color: var(--brand-blue);
  }
  .call-box {
    position: absolute; left: 104px; top: 502px; width: 228px; height: 63px;
    border: 1px solid #8e8e8e; text-align: center;
  }
  .call-box__legend {
    position: absolute; top: -10px; left: 50%; transform: translateX(-50%);
    background: var(--card); padding: 0 5px; font-size: 17px; color: var(--ink); line-height: 1.1;
  }
  .call-box__lines { padding-top: 11px; font-size: 19px; line-height: 23px; color: var(--ink); }
  .accent-blue { color: var(--brand-blue); }

  .phone { position: absolute; left: 40px; top: 590px; display: flex; align-items: center; gap: 8px; }
  .phone__icon { width: 26px; height: 26px; }
  .phone__number { font-size: 19px; font-weight: 700; color: var(--brand-blue); }
  .brand--back { left: 272px; top: 594px; width: 120px; }
  .brand--back .brand__name { font-size: 21px; gap: 5px; }
  .brand--back .brand__dot { width: 7px; height: 7px; }
</style>
</head>
<body>

<section class="flyer flyer--front">
  <div class="hero-photo" role="img" aria-label="Family of four sitting together under a pink umbrella against a bright blue sky with clouds"></div>
  <svg class="hero-curve" viewBox="0 0 434 40" aria-hidden="true">
    <path d="M0 28 L70 12 Q217 4 364 12 L434 32 L434 40 L0 40 Z" fill="var(--card)"/>
    <path d="M0 28 L70 12" stroke="var(--deep-blue)" stroke-width="4" fill="none"/>
    <path d="M364 12 L434 32" stroke="var(--deep-blue)" stroke-width="4" fill="none"/>
  </svg>

  <div class="brand brand--front">
    <span class="brand__name"><span class="brand__dot"></span>Shieldwise</span>
  </div>

  <div class="headline-box"></div>
  <h1 class="headline">
    <span class="headline__line headline__only"><span>The ONLY</span></span>
    <span class="headline__line headline__free">100% FREE</span>
    <span class="headline__line headline__system">SECURITY SYSTEM</span>
  </h1>

  <div class="footer-bar">www.shieldwise-home.com</div>
</section>

<section class="flyer flyer--back">
  <div class="sky-panel"></div>

  <div class="benefit benefit--equipment">
    <svg class="benefit__icon" viewBox="0 0 100 100" aria-hidden="true">
      <circle cx="50" cy="50" r="47" fill="none" stroke="#6b6b6b" stroke-width="3" stroke-dasharray="11 7"/>
      <path d="M50 24 L71 32 V50 C71 63 62 72 50 77 C38 72 29 63 29 50 V32 Z" fill="#fff" stroke="var(--brand-green)" stroke-width="4"/>
      <rect x="41" y="48" width="18" height="14" rx="2" fill="var(--brand-blue)"/>
      <path d="M44 48 V43 a6 6 0 0 1 12 0 V48" fill="none" stroke="var(--brand-blue)" stroke-width="3"/>
    </svg>
    <div class="benefit__text">
      <div class="benefit__title">$100’s in FREE</div>
      <div class="benefit__note">Premium Security Equipment</div>
    </div>
  </div>

  <div class="benefit benefit--install">
    <svg class="benefit__icon" viewBox="0 0 100 100" aria-hidden="true">
      <circle cx="50" cy="50" r="47" fill="none" stroke="#6b6b6b" stroke-width="3" stroke-dasharray="11 7"/>
      <rect x="28" y="28" width="26" height="44" rx="2" fill="none" stroke="var(--brand-green)" stroke-width="4"/>
      <path d="M41 34 V44 M37 40 L41 44 L45 40" stroke="var(--brand-green)" stroke-width="3" fill="none"/>
      <rect x="36" y="52" width="10" height="14" rx="2" fill="var(--brand-blue)"/>
      <path d="M62 40 L74 52 M68 34 a7 7 0 1 0 8 8 L71 47 L65 41 Z" fill="var(--brand-green)" stroke="var(--brand-green)" stroke-width="3" stroke-linejoin="round"/>
    </svg>
    <div class="benefit__text">
      <div class="benefit__title">FREE Installation</div>
      <div class="benefit__note">And what no other company offers</div>
    </div>
  </div>

  <div class="benefit benefit--monitoring">
    <svg class="benefit__icon" viewBox="0 0 100 100" aria-hidden="true">
      <circle cx="50" cy="50" r="47" fill="none" stroke="#6b6b6b" stroke-width="3" stroke-dasharray="11 7"/>
      <circle cx="50" cy="54" r="20" fill="var(--brand-green)"/>
      <text x="50" y="62" text-anchor="middle" font-family="Lato, sans-serif" font-weight="700" font-size="22" fill="#fff">$</text>
      <circle cx="40" cy="28" r="8" fill="var(--brand-blue)"/>
    </svg>
    <div class="benefit__text">
      <div class="benefit__title benefit__title--sm">ZERO Cost Monitoring</div>
      <div class="benefit__note benefit__note--light">(up to a <span class="accent-green">$74.95</span> per month value)</div>
    </div>
  </div>

  <p class="how-question">HOW ARE WE ABLE TO DO THIS?</p>
  <div class="call-box">
    <span class="call-box__legend">CALL OUR</span>
    <div class="call-box__lines">
      <div><span class="accent-blue">24-hour</span> message line</div>
      <div>for a <span class="accent-green">3-minute</span> overview</div>
    </div>
  </div>

  <div class="phone">
    <svg class="phone__icon" viewBox="0 0 26 26" aria-hidden="true">
      <circle cx="13" cy="13" r="13" fill="var(--brand-green)"/>
      <path d="M9 7 L11 7 L12 10 L10.5 11.5 C11.5 13.5 12.5 14.5 14.5 15.5 L16 14 L19 15 L19 17 C19 18 18 19 17 19 C12 18.5 7.5 14 7 9 C7 8 8 7 9 7 Z" fill="#fff"/>
    </svg>
    <span class="phone__number">+1 555-014-2283</span>
  </div>

  <div class="brand brand--back">
    <span class="brand__name"><span class="brand__dot"></span>Shieldwise</span>
  </div>

  <div class="footer-bar">www.shieldwise-home.com</div>
</section>

</body>
</html>
```